Profesional personal website needs design and business card

I need a business card with my professional name as a logo "Marlo Vitality" for my business. I am a Wellness Coach, consultant and trainer. So it should be professional, wellness oriented and modern.

Target Market(s)

Private clients, governments, corporations. Luxury and high market.

Industry/Entity Type

Health And Wellness

Contact Information for Business Card

Marlo Vitality should be the logo

Colors

Designer to choose colors to be used in the design.

Requirements
Must have
• Marlo Vitality
• Name: Tomás Arribal
• Wellness Coach, Consultant & Trainer.
• Website: www.marlovitality.example
• Phone:
• Spain (+34) 612 480 397
• (USA) +1 (555) 318 2046
Nice to have
• The most important is the design of "Marlo Vitality", as this is going to be my personal brand logo. It should be professional, wellness, high end and actual.
Should not have
• no golds, no baroque style..

```html
<!DOCTYPE html>
<html lang="en">
<head>
<meta charset="utf-8">
<title>Marlo Vitality — Business Card</title>
<link rel="stylesheet" href="https://fonts.googleapis.com/css2?family=Barlow:wght@600;700&family=Barlow+Condensed:wght@400;500&display=swap">
<style>
  :root {
    --page: #ffffff;
    --card: #1c1c1c;
    --ink: #ffffff;
    --accent: #c9d300;
    --silver: #cfcfcf;
  }
  * { box-sizing: border-box; margin: 0; padding: 0; }
  html, body { width: 1200px; height: 1200px; overflow: hidden; background: var(--page); }
  .sheet { position: relative; width: 1200px; height: 1200px; }

  .card {
    position: absolute; left: 150px; width: 900px; height: 514px;
    background: var(--card); overflow: hidden;
    box-shadow: 0 14px 30px rgba(0,0,0,0.18);
  }
  .card--front { top: 60px; }
  .card--back { top: 626px; }

  .decor { position: absolute; border-radius: 50%; }
  .decor--bloom {
    background: radial-gradient(circle, rgba(201,211,0,0.85) 0%, rgba(201,211,0,0.45) 40%, rgba(207,207,207,0.25) 60%, rgba(28,28,28,0) 72%);
  }
  .decor--bud {
    background: radial-gradient(circle, rgba(207,207,207,0.7) 0%, rgba(201,211,0,0.35) 45%, rgba(28,28,28,0) 70%);
  }

  .brand {
    position: absolute; left: 0; right: 0; top: 218px; text-align: center;
  }
  .brand__name {
    font-family: "Barlow", sans-serif; font-weight: 700;
    font-size: 64px; color: var(--ink); letter-spacing: 1px; line-height: 1;
  }
  .brand__url {
    margin-top: 10px;
    font-family: "Barlow Condensed", sans-serif; font-weight: 500;
    font-size: 22px; color: var(--accent); letter-spacing: 6px;
  }

  .contact {
    position: absolute; right: 70px; top: 150px; text-align: right; width: 520px;
  }
  .contact__name {
    font-family: "Barlow", sans-serif; font-weight: 700;
    font-size: 46px; color: var(--ink); line-height: 1.05;
  }
  .contact__role {
    font-family: "Barlow Condensed", sans-serif; font-weight: 400;
    font-size: 28px; color: var(--accent); margin-top: 4px;
  }
  .contact__rule {
    height: 2px; margin: 12px 0 16px auto; width: 440px;
    background: linear-gradient(to right, rgba(255,255,255,0), var(--ink));
  }
  .contact__phone {
    font-family: "Barlow Condensed", sans-serif; font-weight: 400;
    font-size: 30px; color: var(--ink); line-height: 1.25;
  }
  .contact__country { color: var(--accent); font-weight: 500; margin-right: 6px; }
</style>
</head>
<body>
<main class="sheet">

  <section class="card card--front" aria-label="Business card front">
    <div class="decor decor--bud" role="img" aria-label="Small white and lime floral ornament" style="left:560px; top:70px; width:90px; height:90px;"></div>
    <div class="decor decor--bloom" role="img" aria-label="Lime and white floral ornament" style="left:640px; top:80px; width:190px; height:190px;"></div>
    <div class="decor decor--bud" role="img" aria-label="Small white and lime floral ornament" style="left:740px; top:20px; width:90px; height:90px;"></div>
    <div class="decor decor--bud" role="img" aria-label="Small white and lime floral ornament" style="left:790px; top:170px; width:90px; height:90px;"></div>
    <div class="decor decor--bloom" role="img" aria-label="Large lime and white floral ornament" style="left:-110px; top:330px; width:330px; height:330px;"></div>

    <div class="brand">
      <p class="brand__name">Marlo Vitality</p>
      <p class="brand__url">www.marlovitality.example</p>
    </div>
  </section>

  <section class="card card--back" aria-label="Business card back">
    <div class="decor decor--bloom" role="img" aria-label="Large lime and white floral ornament" style="left:0px; top:70px; width:400px; height:400px;"></div>
    <div class="decor decor--bud" role="img" aria-label="Small white and lime floral ornament" style="left:290px; top:40px; width:80px; height:80px;"></div>
    <div class="decor decor--bud" role="img" aria-label="Small white and lime floral ornament" style="left:120px; top:420px; width:80px; height:80px;"></div>

    <div class="contact">
      <p class="contact__name">Tomás Arribal</p>
      <p class="contact__role">Wellness Coach, Consultant &amp; Trainer</p>
      <div class="contact__rule"></div>
      <p class="contact__phone"><span class="contact__country">Spain</span>(+34) 612 480 397</p>
      <p class="contact__phone"><span class="contact__country">USA</span>+1 (555) 318 2046</p>
    </div>
  </section>

</main>
</body>
</html>
```